Financial PR company Homepage and Inner Page design

Please design a web homepage and innerpage for OVIN Public Relations.
OVIN Public Relations is a Financial PR company targeting Shenzhen Qian Special Economical Zone.
Note:
1. Menu includes ( Please specialize in Chinese and we want to see the Chinese fonts)
关于我们/服务板块/专业优势/合作伙伴/前海商圈/公司新闻/加盟我们/联系我们

2. Please refer to world class PR Business company and contribute your idea on website design and color themes.

3. We have attached the Logo for reference.

4. Anytime use picture for reference, please select asian business people pictures.

Cheers,

HI Designers, Thanks for the design submission. Here is our client feedback: 1. Adopt one screen design. 2. Use amiable Asia Business woman pictures. 3. Use contrastive color theme for the design. Cheers, Kip From TW

```html
<!DOCTYPE html>
<html lang="zh">
<head>
<meta charset="utf-8">
<title>OVIN PR — Qianhai PR Experts</title>
<link rel="stylesheet" href="https://fonts.googleapis.com/css2?family=Figtree:wght@300;400;500;600&family=Noto+Sans+SC:wght@500;700&display=swap">
<style>
:root{
  --black:#000;
  --white:#fff;
  --sky:#4fb3e8;
  --nav-active:#3aa6e0;
  --card:rgba(236,233,240,.86);
  --card-title:#555;
  --card-text:#666;
  --footer-text:#d8d8d8;
  --rule:#333;
}
*{margin:0;padding:0;box-sizing:border-box}
html,body{width:1200px;height:1062px;overflow:hidden;background:var(--black)}
body{font-family:"Figtree",sans-serif;color:var(--white);position:relative}
.site-header{position:absolute;left:0;top:0;width:1200px;height:87px;background:var(--black)}
.brand{position:absolute;left:148px;top:6px;width:228px;height:74px}
.brand-mark{position:absolute;left:4px;top:10px;width:58px;height:58px;border-radius:50%;background:var(--sky)}
.brand-name{position:absolute;left:86px;top:2px;font-size:34px;font-weight:400;color:var(--white);letter-spacing:.5px;line-height:1}
.brand-tag{position:absolute;left:86px;top:37px;font-size:17px;font-weight:300;color:var(--white);line-height:1}
.brand-cn{position:absolute;right:5px;top:56px;font-family:"Noto Sans SC",sans-serif;font-size:12px;font-weight:700;color:var(--sky);line-height:1}
.main-nav{position:absolute;left:487px;top:31px;display:flex;gap:0}
.main-nav a{font-family:"Noto Sans SC",sans-serif;font-size:13px;font-weight:700;color:var(--white);text-decoration:none;margin-right:18px;line-height:18px}
.main-nav a.is-active{color:var(--nav-active)}
.hero{position:absolute;left:0;top:87px;width:1200px;height:814px;
  background:
   radial-gradient(ellipse at 10% 75%,rgba(200,60,110,.45),transparent 45%),
   radial-gradient(ellipse at 90% 85%,rgba(190,60,120,.4),transparent 40%),
   radial-gradient(ellipse at 50% 30%,rgba(90,100,140,.5),transparent 60%),
   linear-gradient(180deg,#2b3345 0%,#2a2d44 40%,#3a2e4e 75%,#54385a 100%)}
.hero-title{position:absolute;left:0;width:1200px;top:116px;text-align:center;font-size:56px;font-weight:400;letter-spacing:1px;line-height:1}
.hero-sub{position:absolute;left:0;width:1200px;top:186px;text-align:center;font-size:31px;font-weight:400;line-height:1}
.hero-lead{position:absolute;left:230px;width:740px;top:227px;text-align:center;font-size:16px;line-height:22px}
.btn{position:absolute;top:312px;height:46px;font-size:19px;line-height:46px;text-align:center;color:var(--white)}
.btn-primary{left:457px;width:172px;background:var(--sky)}
.btn-outline{left:658px;width:174px;border:1px solid var(--white);line-height:44px}
.feature{position:absolute;top:458px;width:266px;height:291px;background:var(--card);text-align:center}
.feature-photo{display:block;margin:23px auto 0;width:230px;height:119px;border:1px solid var(--white)}
.feature h2{margin-top:19px;font-size:20px;font-weight:400;color:var(--card-title)}
.feature p{margin-top:13px;font-size:11.5px;line-height:20px;color:var(--card-text)}
.feature .readmore{display:block;margin-top:8px;font-size:12px;font-weight:500;color:#111}
.f1{left:148px}.f2{left:467px}.f3{left:787px}
.site-footer{position:absolute;left:0;top:901px;width:1200px;height:161px;background:var(--black);color:var(--footer-text)}
.foot-links{position:absolute;left:150px;top:46px;font-size:13px}
.foot-links span{margin:0 5px;color:#aaa}
.contact{position:absolute;right:148px;top:44px;display:flex;align-items:center;font-size:13px}
.contact svg{margin-right:16px}
.contact .gap{margin-left:20px}
.rule{position:absolute;left:0;top:99px;width:1200px;height:1px;background:var(--rule)}
.copyright{position:absolute;left:149px;top:120px;font-size:12px}
.social{position:absolute;right:148px;top:117px;display:flex;gap:8px}
.social i{display:block;width:20px;height:20px;border-radius:50%;background:#cfcfcf}
</style>
</head>
<body>
<header class="site-header">
  <div class="brand">
    <span class="brand-mark"></span>
    <span class="brand-name">OVIN PR</span>
    <span class="brand-tag">qianhai pr experts</span>
    <span class="brand-cn">前海奥文公关</span>
  </div>
  <nav class="main-nav">
    <a class="is-active" href="#">首页</a>
    <a href="#">关于我们</a>
    <a href="#">服务板块</a>
    <a href="#">专业优势</a>
    <a href="#">作伙伴</a>
    <a href="#">前海商圈</a>
    <a href="#">公司新闻</a>
    <a href="#">加盟我们</a>
    <a href="#">联系我们</a>
  </nav>
</header>

<section class="hero" role="img" aria-label="Night skyline of Shenzhen with lit skyscrapers">
  <h1 class="hero-title">WELCOME TO OVIN PR</h1>
  <p class="hero-sub">QIANHAI PR EXPERTS</p>
  <p class="hero-lead">Lorem ipsum dolor sit amet, consectetuer adipiscing elit, sed diam nonummy nibh euismod tincidunt ut laoreet dolore magna aliquam erat volutpat. Ut wisi enim ad minim veniam, quis nostrud</p>
  <span class="btn btn-primary">Learn More</span>
  <span class="btn btn-outline">Get A Qoute</span>

  <article class="feature f1">
    <div class="feature-photo" role="img" aria-label="Smiling businesswoman at an office desk" style="background:linear-gradient(135deg,#9cc9e6,#e8eef4 60%,#c9d7e2)"></div>
    <h2>Who We Are?</h2>
    <p>Lorem ipsum dolor sit amet,<br>consectetuer adipiscing elit, sed diam<br>nonummy nibh euismod tincidunt ut</p>
    <span class="readmore">READMORE</span>
  </article>
  <article class="feature f2">
    <div class="feature-photo" role="img" aria-label="Businesswoman working on a laptop in an office" style="background:linear-gradient(135deg,#6b5a48,#d9d2c4 55%,#8a7b68)"></div>
    <h2>What We Do?</h2>
    <p>Lorem ipsum dolor sit amet,<br>consectetuer adipiscing elit, sed diam<br>nonummy nibh euismod tincidunt ut</p>
    <span class="readmore">READMORE</span>
  </article>
  <article class="feature f3">
    <div class="feature-photo" role="img" aria-label="Businesswoman talking on a phone outside an office building" style="background:linear-gradient(135deg,#cfd6dc,#8a8f96 55%,#2a2a2e)"></div>
    <h2>Why Trust Us?</h2>
    <p>Lorem ipsum dolor sit amet,<br>consectetuer adipiscing elit, sed diam<br>nonummy nibh euismod tincidunt ut</p>
    <span class="readmore">READMORE</span>
  </article>
</section>

<footer class="site-footer">
  <div class="foot-links">Home<span>|</span>About Us<span>|</span>Service<span>|</span>Join Us<span>|</span>Contact Us</div>
  <div class="contact">
    <svg width="12" height="12" viewBox="0 0 24 24"><path fill="#bbb" d="M6.6 10.8a15 15 0 0 0 6.6 6.6l2.2-2.2a1 1 0 0 1 1-.25 11 11 0 0 0 3.6.6 1 1 0 0 1 1 1V20a1 1 0 0 1-1 1A17 17 0 0 1 3 4a1 1 0 0 1 1-1h3.5a1 1 0 0 1 1 1 11 11 0 0 0 .6 3.6 1 1 0 0 1-.25 1z"/></svg>
    <span>123-456-78901</span>
    <svg class="gap" width="13" height="10" viewBox="0 0 26 20"><rect width="26" height="20" fill="#bbb"/><path d="M0 0l13 10L26 0" fill="none" stroke="#000" stroke-width="2"/></svg>
    <span>mail@demo.com</span>
  </div>
  <div class="rule"></div>
  <div class="copyright">Copyright © OVIN PR 2014 All Rights Reserved</div>
  <div class="social"><i></i><i></i><i></i><i></i></div>
</footer>
</body>
</html>
```